Redesign Application Page for Job Position

Would like to get a redesign on our Job Application Page.
You can use corvanheights or brendolix as references.

http://www.careersatxlm.example/XLM/NCreateAccount.aspx?aga=qtrwkz4hopLM7

Target Market(s)

Professional Security Individuals

Industry/Entity Type

Security Guard

Coding

Coded - Design and coding required

Number of Pages Required

1 page

Font styles to use
Sans Serif

Colors
0255a3
3276b5
ffcf3e
fee18a

Requirements
Must have
• User Friendly, Easy Navigation. Must be very easy to read and understand what is required or missing.
Should not have
• Ugly or Bulky

```html
<!DOCTYPE html>
<html lang="en">
<head>
<meta charset="utf-8">
<title>Crestline Guard Services – Create An Application</title>
<link rel="stylesheet" href="https://fonts.googleapis.com/css2?family=Roboto+Condensed:wght@400;700&family=Roboto:wght@400;500;700&display=swap">
<style>
:root{
  --navy:#1d1a40;
  --gold:#f2c21b;
  --red:#e0282e;
  --ink:#333338;
  --label:#3c3c42;
  --muted:#a9a9ad;
  --line:#c4c4c8;
  --band:#efefef;
  --head:#9e9c9f;
  --footer:#232323;
  --white:#ffffff;
}
*{box-sizing:border-box;margin:0;padding:0}
html,body{width:1200px;height:2965px;overflow:hidden}
body{position:relative;background:var(--white);font-family:"Roboto Condensed",Arial,sans-serif;color:var(--ink)}
.abs{position:absolute}

/* top bar */
.topbar{left:0;top:0;width:1200px;height:44px;background:var(--navy);color:var(--white);font-family:Roboto,Arial,sans-serif;font-size:13px}
.contact{top:0;height:44px;display:flex;align-items:center;gap:12px}
.contact svg{width:18px;height:18px}
.social{right:97px;top:13px;display:flex;gap:22px}
.social span{width:18px;height:18px;border-radius:50%;background:var(--gold);display:block}

/* hero */
.hero{left:0;top:44px;width:1200px;height:660px;background:linear-gradient(90deg,#0f1628 0%,#1b2438 30%,#6b5a3e 52%,#c59a4e 70%,#b08a55 85%,#5a6178 100%)}
.brand-mark{left:500px;top:88px;width:200px;text-align:center;font-weight:700;font-size:24px;letter-spacing:1px;color:var(--navy);display:flex;align-items:center;justify-content:center;gap:8px}
.brand-mark i{width:14px;height:14px;background:var(--navy);display:block}
.welcome{right:87px;top:300px;font-size:88px;font-weight:700;color:var(--navy);line-height:1}
.company{right:87px;top:410px;font-size:32px;font-weight:700;color:var(--navy)}
.hero-rule{left:712px;top:474px;width:386px;height:2px;background:var(--gold)}

/* headings */
.section-title{left:0;top:750px;width:1200px;text-align:center;font-size:42px;font-weight:700;letter-spacing:1px;color:#222}
.title-rule{top:779px;height:1px;background:#cfcfcf}
.intro{left:0;top:818px;width:1200px;text-align:center;font-size:23px;color:#666}
.intro em{font-style:normal;color:var(--red)}
.date-label{left:0;top:892px;width:1200px;text-align:center;font-family:Roboto,Arial,sans-serif;font-size:16px;color:#444}
.date-value{left:0;top:922px;width:1200px;text-align:center;font-size:30px;color:#222}

/* fields */
.label{font-family:Roboto,Arial,sans-serif;font-size:16px;color:var(--label)}
.label b{color:var(--red);font-weight:400}
.field{height:34px;border:1px solid var(--line);background:var(--white);font-family:Roboto,Arial,sans-serif;font-size:12px;color:var(--muted);padding:0 10px;display:flex;align-items:center}
.select{justify-content:space-between}
.select::after{content:"";border:6px solid transparent;border-top:7px solid #9a9aa0;margin-top:6px}
.band{left:0;width:1200px;background:var(--band)}

.radio{display:flex;align-items:center;gap:10px;font-size:18px;color:#444}
.radio span{width:13px;height:13px;border-radius:50%;border:1px solid var(--line);display:block;position:relative}
.radio .on::after{content:"";position:absolute;left:3px;top:3px;width:5px;height:5px;border-radius:50%;background:var(--red)}

/* licence table */
.th{height:39px;background:var(--head);color:var(--white);font-family:Roboto,Arial,sans-serif;font-size:14px;display:flex;align-items:center;justify-content:center}
.cell{border:1px solid var(--line);font-family:Roboto,Arial,sans-serif;font-size:13px;color:var(--muted);padding:0 22px;display:flex;align-items:center;line-height:1.8}
.cell.date{padding-left:36px}

.availability{left:0;top:2470px;width:1200px;text-align:center;font-size:25px;color:#444}

/* actions */
.btn{top:2714px;width:201px;height:52px;border-radius:26px;background:var(--navy);color:var(--white);font-size:22px;display:flex;align-items:center;justify-content:center}

/* footer */
.footer{left:0;top:2837px;width:1200px;height:128px;background:var(--footer);color:var(--white);text-align:center}
.help{margin-top:22px;font-size:28px}
.call{margin-top:8px;font-size:28px}
.call span{color:var(--gold)}
</style>
</head>
<body>

<header class="abs topbar">
  <div class="abs contact" style="left:84px">
    <svg viewBox="0 0 18 18"><circle cx="9" cy="9" r="9" fill="#f2c21b"/><rect x="4.5" y="5.5" width="9" height="7" fill="none" stroke="#1d1a40" stroke-width="1.3"/><path d="M4.5 5.5l4.5 4 4.5-4" fill="none" stroke="#1d1a40" stroke-width="1.3"/></svg>
    <span>crestlineguard@mailbox.example</span>
  </div>
  <div class="abs contact" style="left:346px">
    <svg viewBox="0 0 18 18"><circle cx="9" cy="9" r="9" fill="#f2c21b"/><rect x="6" y="4" width="6" height="10" rx="1" fill="none" stroke="#1d1a40" stroke-width="1.3"/></svg>
    <span style="font-weight:700">(310) 555-0148</span>
  </div>
  <nav class="abs social" aria-label="Social links"><span></span><span></span><span></span><span></span><span></span></nav>
</header>

<section class="abs hero" role="img" aria-label="Photo of a security guard in a dark uniform shirt in front of a blurred crowd behind barriers"></section>
<div class="abs brand-mark"><i></i>CRESTLINE</div>
<h1 class="abs welcome">Welcome to</h1>
<div class="abs company">Crestline Guard Services, Inc.</div>
<div class="abs hero-rule"></div>

<h2 class="abs section-title">Create An Application</h2>
<div class="abs title-rule" style="left:257px;width:128px"></div>
<div class="abs title-rule" style="left:810px;width:248px"></div>
<p class="abs intro">Complete all required fields <em>(colored red)</em>, then click "Continue" to create your account!</p>
<div class="abs date-label">Date Created:</div>
<div class="abs date-value">03-Jan-2018</div>

<!-- personal -->
<div class="abs label" style="left:200px;top:1012px">First Name: <b>*</b></div>
<div class="abs field" style="left:200px;top:1046px;width:367px"></div>
<div class="abs label" style="left:633px;top:1012px">Middle Name:</div>
<div class="abs field" style="left:633px;top:1046px;width:365px"></div>

<div class="abs label" style="left:107px;top:1127px">Last Name: <b>*</b></div>
<div class="abs field" style="left:107px;top:1160px;width:367px"></div>
<div class="abs label" style="left:550px;top:1127px">Gender :</div>
<div class="abs radio" style="left:550px;top:1169px"><span></span>Male</div>
<div class="abs radio" style="left:630px;top:1169px"><span class="on"></span>Female</div>
<div class="abs label" style="left:767px;top:1127px">D.O.B :</div>
<div class="abs field" style="left:769px;top:1160px;width:95px">D/D...</div>
<div class="abs field" style="left:884px;top:1160px;width:95px">M/M...</div>
<div class="abs field" style="left:1000px;top:1160px;width:93px">Y/Y...</div>

<!-- address -->
<div class="abs band" style="top:1257px;height:331px"></div>
<div class="abs label" style="left:85px;top:1328px">Street Address: <b>*</b></div>
<div class="abs field" style="left:85px;top:1362px;width:304px"></div>
<div class="abs label" style="left:449px;top:1328px">City:</div>
<div class="abs field" style="left:449px;top:1362px;width:304px"></div>
<div class="abs label" style="left:807px;top:1328px">State:</div>
<div class="abs field" style="left:807px;top:1362px;width:304px"></div>
<div class="abs label" style="left:265px;top:1439px">Nearest Office:</div>
<div class="abs field" style="left:265px;top:1473px;width:306px"></div>
<div class="abs label" style="left:631px;top:1439px">Zip: <b>*</b></div>
<div class="abs field" style="left:631px;top:1473px;width:304px"></div>

<!-- contact & job -->
<div class="abs label" style="left:113px;top:1635px">Phone Number :</div>
<div class="abs field" style="left:113px;top:1671px;width:166px">Cell...</div>
<div class="abs field" style="left:306px;top:1671px;width:165px">Home...</div>
<div class="abs label" style="left:540px;top:1635px">Job Position :</div>
<div class="abs field" style="left:540px;top:1671px;width:304px"></div>
<div class="abs label" style="left:923px;top:1635px">SSN :</div>
<div class="abs field" style="left:923px;top:1671px;width:164px"></div>

<!-- licences -->
<div class="abs label" style="left:85px;top:1777px">License Details :</div>
<div class="abs th" style="left:85px;top:1823px;width:364px">Type</div>
<div class="abs th" style="left:474px;top:1823px;width:329px">Number</div>
<div class="abs th" style="left:826px;top:1823px;width:285px">Expire Date</div>

<div class="abs cell" style="left:85px;top:1878px;width:364px;height:40px">Guard Card</div>
<div class="abs cell" style="left:474px;top:1878px;width:329px;height:40px"></div>
<div class="abs cell date" style="left:826px;top:1878px;width:285px;height:40px">DD / MM / YYYY</div>

<div class="abs cell" style="left:85px;top:1935px;width:364px;height:40px">Baton</div>
<div class="abs cell" style="left:474px;top:1935px;width:329px;height:40px"></div>
<div class="abs cell date" style="left:826px;top:1935px;width:285px;height:40px">DD / MM / YYYY</div>

<div class="abs cell" style="left:85px;top:1993px;width:364px;height:40px">Gun Permit</div>
<div class="abs cell" style="left:474px;top:1993px;width:329px;height:40px"></div>
<div class="abs cell date" style="left:826px;top:1993px;width:285px;height:40px">DD / MM / YYYY</div>

<div class="abs cell" style="left:85px;top:2050px;width:364px;height:40px">Transportation Workers Identification Card (TWIC)</div>
<div class="abs cell" style="left:474px;top:2050px;width:329px;height:40px"></div>
<div class="abs cell date" style="left:826px;top:2050px;width:285px;height:40px">DD / MM / YYYY</div>

<div class="abs cell" style="left:85px;top:2107px;width:364px;height:40px">Merchant Mariner Credential (MMC)</div>
<div class="abs cell" style="left:474px;top:2107px;width:329px;height:40px"></div>
<div class="abs cell date" style="left:826px;top:2107px;width:285px;height:40px">DD / MM / YYYY</div>

<div class="abs cell" style="left:85px;top:2161px;width:364px;height:67px;align-items:flex-start;padding-top:8px">Standards of Training, Certification and Watchkeeping for Seafarers (SCTW)</div>
<div class="abs cell" style="left:474px;top:2161px;width:329px;height:67px"></div>
<div class="abs cell date" style="left:826px;top:2161px;width:285px;height:67px;align-items:flex-start;padding-top:8px">DD / MM / YYYY</div>

<!-- extras -->
<div class="abs label" style="left:85px;top:2325px">ID Document Type :</div>
<div class="abs field select" style="left:85px;top:2361px;width:235px">Select...</div>
<div class="abs label" style="left:348px;top:2325px">Additional Languages :</div>
<div class="abs field select" style="left:348px;top:2361px;width:235px">Select...</div>
<div class="abs label" style="left:613px;top:2325px">Email : <b>*</b></div>
<div class="abs field" style="left:613px;top:2361px;width:233px"></div>
<div class="abs label" style="left:876px;top:2325px">How did you hear about us?</div>
<div class="abs field select" style="left:876px;top:2361px;width:235px">Select...</div>

<!-- availability -->
<div class="abs availability">Work Availability</div>
<div class="abs band" style="top:2519px;height:108px"></div>
<div class="abs label" style="left:85px;top:2538px;font-size:15px">Day Shift :</div>
<div class="abs field select" style="left:85px;top:2570px;width:279px">Select a Day...</div>
<div class="abs label" style="left:459px;top:2538px;font-size:15px">Swing Shift :</div>
<div class="abs field select" style="left:459px;top:2570px;width:276px">Select a Day...</div>
<div class="abs label" style="left:832px;top:2538px;font-size:15px">Night Shift :</div>
<div class="abs field select" style="left:832px;top:2570px;width:279px">Select a Day...</div>

<!-- actions -->
<div class="abs btn" style="left:380px">Continue</div>
<div class="abs btn" style="left:619px">Discard</div>

<footer class="abs footer">
  <div class="help">Need Help?</div>
  <div class="call"><span>Call Us</span> at: (310) 555-0148</div>
</footer>

</body>
</html>
```